Fashion Company Business Card

Style// Minimalism (Less is more)
Colour// No required colour. If you use a solid colour, vigorous violet is preferred, or any other mix of fashionable patterns. Purple reference to http://cdn.pixelvantor.example/blog/Famous-Purple-Logos/11-famous-purple-logos.jpg)
Font// any matching sans serif fonts (logo is helveica neue light)
Contents// as following
- logo
- (website) www.morbelle.com
- (add) 3870 Glenwick Ave, Suite 415 Toronto ON M4T 1K8
- (Office phone) +1 416 555 0173
- (email) info@morbelle.com
- (social media logos: Facebook, Instagram, Twitter, Tumblr, Vimeo, Youtube) @Morbelle/@Morbellemedia
- (slogan)│Fashion│Art│Unique
*optional - QR code
- (personal info) For example
Tessa Korby
Founder & Creative Director
c. XXX.XXX.XXXX
Please submit jpg file for selecting, and submit a psd file for editing personal info for different employers after selected. If you need more information, please email tessakorby@morbelle.com.

```html
<!DOCTYPE html>
<html lang="en">
<head>
<meta charset="utf-8">
<title>Morbelle Business Card</title>
<link rel="stylesheet" href="https://fonts.googleapis.com/css2?family=Inter:wght@300;400;700&display=swap">
<style>
  :root {
    --page-bg: #ecebe9;
    --ink: #111111;
    --muted-ink: #222222;
    --lavender: #d9d0e6;
    --cream: #f7f3e8;
    --blush: #ecc6dc;
    --card-white: #ffffff;
    --rule: #e3dfea;
    --icon-grey: #a9a9ad;
  }
  * { box-sizing: border-box; margin: 0; padding: 0; }
  html, body {
    width: 1200px;
    height: 1000px;
    overflow: hidden;
    background: var(--page-bg);
    font-family: "Inter", "Helvetica Neue", Arial, sans-serif;
    color: var(--ink);
  }
  .canvas { position: relative; width: 1200px; height: 1000px; }

  .card {
    position: absolute;
    width: 765px;
    height: 472px;
    overflow: hidden;
    box-shadow: 0 2px 8px rgba(0,0,0,0.18);
    background: var(--card-white);
  }
  .card--front { left: 47px; top: 48px; }
  .card--back  { left: 371px; top: 476px; }

  .card__texture {
    position: absolute;
    inset: 0;
    background:
      radial-gradient(ellipse at 15% 8%, rgba(236,198,220,0.55), transparent 35%),
      radial-gradient(ellipse at 85% 92%, rgba(236,198,220,0.45), transparent 35%),
      linear-gradient(180deg,
        var(--lavender) 0%,
        var(--cream) 18%,
        var(--card-white) 38%,
        var(--card-white) 62%,
        var(--cream) 80%,
        var(--lavender) 100%);
  }

  .wordmark {
    position: absolute;
    font-weight: 300;
    color: var(--ink);
    letter-spacing: 4px;
    white-space: nowrap;
    transform: translateX(-50%);
  }
  .card--front .wordmark { left: 383px; top: 218px; font-size: 52px; }
  .card--back .wordmark  { left: 382px; top: 112px; font-size: 46px; }

  .website {
    position: absolute;
    left: 382px; top: 164px;
    transform: translateX(-50%);
    font-size: 18px;
    font-weight: 400;
    color: var(--ink);
  }

  .slogan-band {
    position: absolute;
    left: 0; right: 0;
    top: 193px; height: 50px;
    background: rgba(255,255,255,0.85);
    border-top: 2px solid var(--rule);
    border-bottom: 2px solid var(--rule);
    display: flex;
    align-items: center;
    justify-content: center;
  }
  .slogan {
    font-size: 28px;
    font-weight: 400;
    letter-spacing: 7px;
    color: var(--ink);
    white-space: nowrap;
  }

  .person {
    position: absolute;
    left: 209px; top: 250px;
    transform: translateX(-50%);
    text-align: center;
    white-space: nowrap;
  }
  .person__name { font-size: 33px; font-weight: 700; line-height: 40px; }
  .person__title { font-size: 25px; font-weight: 400; line-height: 32px; }
  .person__cell { font-size: 21px; font-weight: 400; line-height: 28px; }

  .office {
    position: absolute;
    left: 579px; top: 262px;
    transform: translateX(-50%);
    text-align: center;
    white-space: nowrap;
    font-size: 17px;
    line-height: 24px;
    color: var(--muted-ink);
  }
  .office__contact { margin-top: 8px; }

  .social {
    position: absolute;
    left: 382px; top: 364px;
    transform: translateX(-50%);
    text-align: center;
  }
  .social__icons { display: flex; gap: 5px; justify-content: center; }
  .social__icon { width: 30px; height: 30px; background: var(--icon-grey); }
  .social__handles {
    margin-top: 10px;
    font-size: 13px;
    color: var(--muted-ink);
    word-spacing: 18px;
    white-space: nowrap;
  }
</style>
</head>
<body>
<div class="canvas">

  <section class="card card--front">
    <div class="card__texture" role="img" aria-label="Soft faceted lavender and cream crystal pattern"></div>
    <div class="wordmark">MORBELLE</div>
  </section>

  <section class="card card--back">
    <div class="card__texture" role="img" aria-label="Soft faceted lavender and cream crystal pattern"></div>
    <div class="wordmark">MORBELLE</div>
    <div class="website">www.morbelle.com</div>

    <div class="slogan-band">
      <p class="slogan">FASHION | ART | UNIQUE</p>
    </div>

    <div class="person">
      <p class="person__name">Tessa Korby</p>
      <p class="person__title">Founder &amp; Creative Director</p>
      <p class="person__cell">c. XXX.XXX.XXXX</p>
    </div>

    <div class="office">
      <p>3870 Glenwick Ave, Suite 415</p>
      <p>Toronto ON M4T 1K8</p>
      <p class="office__contact">+1 416 555 0173 &#9679; info@morbelle.com</p>
    </div>

    <div class="social">
      <div class="social__icons" aria-label="Social media links">
        <span class="social__icon"></span>
        <span class="social__icon"></span>
        <span class="social__icon"></span>
        <span class="social__icon"></span>
        <span class="social__icon"></span>
        <span class="social__icon"></span>
      </div>
      <p class="social__handles">@Morbelle @Morbellemedia</p>
    </div>
  </section>

</div>
</body>
</html>
```